Hot Offer banner for product listing page

Hi, we need a banner in the dimensions 210x390px which will be shown in the product listing on our online shop. There are 18 products and in between randomly there should be 3 banners with three different information.
first banner: fast delivery
The idea is to show a stove which is very "fast". Maybe you can make an effect like in Voidcruiser Halcyon when they activate the warp drive or something similar. Anyway, the banner should indicate that the delivery is very fast for this product.

second banner: Advantage banner
We would like to have a banner which names all our advantages in our online shop. this is the list of advantages:
- over 200,000 satisfied customers
- Best price guarantee
- thousands of devices in stock
- Top ratings

I attached you some examples, just to give you an idea.

```html
<!DOCTYPE html>
<html lang="de">
<head>
<meta charset="utf-8">
<title>Kaminofen Banner</title>
<link rel="stylesheet" href="https://fonts.googleapis.com/css2?family=Roboto:wght@500;700&display=swap">
<style>
  :root {
    --page: #f3efe8;
    --orange: #f39200;
    --orange-light: #f7a51c;
    --orange-deep: #ec8400;
    --panel-grey: #e6e6e9;
    --wave-grey: #e4e4e7;
    --text-grey: #575757;
    --white: #ffffff;
    --photo-dark: #1d1d1f;
    --photo-mid: #3c3c40;
  }
  * { margin: 0; padding: 0; box-sizing: border-box; }
  html, body {
    width: 1200px; height: 999px; overflow: hidden;
    background: var(--page);
    font-family: "Roboto", Arial, sans-serif;
  }
  .canvas { position: relative; width: 1200px; height: 999px; }
  .banner {
    position: absolute; top: 124px;
    width: 394px; height: 731px; overflow: hidden;
  }
  .banner svg.shapes { position: absolute; inset: 0; width: 100%; height: 100%; }

  /* Delivery banner */
  .banner--delivery { left: 161px; background: var(--panel-grey); }
  .delivery-title {
    position: absolute; left: 0; right: 0; text-align: center;
    font-weight: 700; line-height: 1;
  }
  .delivery-title--product { top: 530px; font-size: 50px; color: var(--orange); }
  .delivery-title--status { top: 600px; font-size: 42px; color: var(--text-grey); font-weight: 500; }

  /* Advantages banner */
  .banner--advantages {
    left: 632px;
    background: linear-gradient(160deg, var(--orange-light) 0%, var(--orange) 55%, var(--orange-deep) 100%);
  }
  .advantage-label {
    position: absolute; color: var(--white);
    font-weight: 700; font-size: 23px; line-height: 1.45;
    transform: translateY(-50%);
  }
</style>
</head>
<body>
<main class="canvas">

  <section class="banner banner--delivery">
    <svg class="shapes" viewBox="0 0 210 390" preserveAspectRatio="none">
      <defs>
        <linearGradient id="stovePhotoTone" x1="0" y1="0" x2="1" y2="1">
          <stop offset="0" stop-color="var(--photo-mid)"/>
          <stop offset="0.55" stop-color="#8a8a90"/>
          <stop offset="1" stop-color="var(--photo-dark)"/>
        </linearGradient>
      </defs>
      <path class="photo-frame" d="M102 0 C52 14 30 90 34 150 C38 212 68 252 96 264 H210 V0 Z" fill="var(--orange)"/>
      <path class="stove-photo" role="img" aria-label="Foto eines grauen Kaminofens mit brennendem Feuer vor dunklem Hintergrund"
            d="M108 0 C62 16 38 90 41 150 C44 208 72 246 98 262 H210 V0 Z" fill="url(#stovePhotoTone)"/>
      <path class="wave wave--white" d="M0 362 Q55 334 115 352 T210 340 V390 H0 Z" fill="var(--white)"/>
      <path class="wave wave--orange" d="M0 378 Q60 356 122 374 T210 366 V390 H0 Z" fill="var(--orange)"/>
    </svg>
    <h2 class="delivery-title delivery-title--product">Kaminofen</h2>
    <p class="delivery-title delivery-title--status">sofort lieferbar</p>
  </section>

  <section class="banner banner--advantages">
    <svg class="shapes" viewBox="0 0 210 390" preserveAspectRatio="none">
      <g class="connector" fill="none" stroke="var(--white)" stroke-width="0.9">
        <path d="M31 75 V86 Q31 92 37 92 H171 Q177 92 177 98 V110"/>
        <path d="M177 160 V172 Q177 178 171 178 H37 Q31 178 31 184 V198"/>
        <path d="M31 248 V258 Q31 264 37 264 H171 Q177 264 177 270 V285"/>
      </g>

      <g class="icon icon--customers" transform="translate(31 50)">
        <circle r="25" fill="var(--white)"/>
        <circle r="19" fill="var(--orange)"/>
        <g fill="var(--white)">
          <circle cx="-7" cy="-4" r="3"/><circle cx="7" cy="-4" r="3"/><circle cx="0" cy="-6" r="3.6"/>
          <path d="M-12 7 Q-12 0 -7 0 Q-2 0 -2 7 Z"/>
          <path d="M2 7 Q2 0 7 0 Q12 0 12 7 Z"/>
          <path d="M-6 8 Q-6 -1 0 -1 Q6 -1 6 8 Z"/>
        </g>
      </g>

      <g class="icon icon--price" transform="translate(177 135)">
        <circle r="25" fill="var(--white)"/>
        <circle r="19" fill="var(--orange)"/>
        <circle r="12" fill="none" stroke="var(--white)" stroke-width="1.6" stroke-dasharray="2.2 1.4"/>
        <circle r="8" fill="var(--white)"/>
        <text y="3.6" text-anchor="middle" font-size="10" font-weight="700" fill="var(--orange)" font-family="Roboto, Arial, sans-serif">$</text>
      </g>

      <g class="icon icon--stock" transform="translate(31 223)">
        <circle r="25" fill="var(--white)"/>
        <circle r="19" fill="var(--orange)"/>
        <g fill="var(--white)">
          <rect x="-5" y="-11" width="10" height="9" rx="1"/>
          <rect x="-11" y="0" width="10" height="9" rx="1"/>
          <rect x="1" y="0" width="10" height="9" rx="1"/>
        </g>
      </g>

      <g class="icon icon--ratings" transform="translate(177 310)">
        <circle r="25" fill="var(--white)"/>
        <circle r="19" fill="var(--orange)"/>
        <g fill="var(--white)">
          <path transform="translate(0 -6) scale(0.7)" d="M0 -9 L2.6 -3 L9 -2.8 L4 1.4 L5.6 8 L0 4.4 L-5.6 8 L-4 1.4 L-9 -2.8 L-2.6 -3 Z"/>
          <path transform="translate(-7 5) scale(0.7)" d="M0 -9 L2.6 -3 L9 -2.8 L4 1.4 L5.6 8 L0 4.4 L-5.6 8 L-4 1.4 L-9 -2.8 L-2.6 -3 Z"/>
          <path transform="translate(7 5) scale(0.7)" d="M0 -9 L2.6 -3 L9 -2.8 L4 1.4 L5.6 8 L0 4.4 L-5.6 8 L-4 1.4 L-9 -2.8 L-2.6 -3 Z"/>
        </g>
      </g>

      <path class="wave wave--grey" d="M0 368 Q50 348 108 364 T210 352 V390 H0 Z" fill="var(--wave-grey)"/>
    </svg>

    <p class="advantage-label" style="left:141px; top:94px;">über 200.000<br>zufriedene Kunden</p>
    <p class="advantage-label" style="left:25px; top:253px;">Bestpreisgarantie</p>
    <p class="advantage-label" style="left:141px; top:418px;">Tausende<br>Geräte auf Lager</p>
    <p class="advantage-label" style="left:25px; top:594px;">Top-Bewertungen</p>
  </section>

</main>
</body>
</html>
```